Zielgruppe
Ich bin eine junge Fotografin und tätig in folgenden Bereichen:
- Hochzeits-Fotografie
- Outdoor-Fotografie
- Studio-Fotografie
Aufgabenstellung
Die Seite soll freundlich, professionell und übersichtlich sein.
Die Seite soll von den Bildern leben. Emotionen vermitteln.
Responsive Design ist mir wichtig, im nachhinein möchte ich die Seite Programmieren lassen damit ich mit Wordpress arbeiten kann und die Seite soll gut Suchmaschinenoptimiert werden.

```html
<!DOCTYPE html>
<html lang="de">
<head>
<meta charset="utf-8">
<title>Velvet Lumen – Hinter der Linse</title>
<link href="https://fonts.googleapis.com/css2?family=Open+Sans:wght@400;600;700&family=Roboto:wght@400&display=swap" rel="stylesheet">
<style>
:root{
  --red:#d0161c;
  --white:#ffffff;
  --black:#000000;
  --header-dark:#1c2a22;
  --header-light:#5e6a55;
  --wood:#6a4630;
  --wood-dark:#2e2119;
  --sweater:#8c8c8a;
}
*{margin:0;padding:0;box-sizing:border-box}
html,body{width:1200px;height:752px;overflow:hidden;background:var(--white)}
body{position:relative;font-family:"Open Sans",sans-serif;color:var(--white)}
.corner{position:absolute;width:80px;height:80px;border-color:var(--red);border-style:solid;border-width:0;z-index:5}
.corner.tl{left:6px;top:6px;border-top-width:2px;border-left-width:2px}
.corner.tr{right:6px;top:6px;border-top-width:2px;border-right-width:2px}
.corner.bl{left:6px;bottom:6px;border-bottom-width:2px;border-left-width:2px}
.corner.br{right:6px;bottom:6px;border-bottom-width:2px;border-right-width:2px}

.site-header{position:absolute;left:6px;top:6px;width:1188px;height:126px;
  background:linear-gradient(90deg,#3b3a2a 0%,var(--header-dark) 18%,#4b5a4c 38%,var(--header-dark) 55%,var(--header-light) 72%,#2a3128 88%,var(--header-dark) 100%)}
.brand{position:absolute;left:194px;top:0;width:130px;height:86px;background:var(--white);
  display:flex;align-items:center;justify-content:center;
  clip-path:polygon(0 0,100% 0,100% 100%,50% 90%,0 100%)}
.brand-name{font-family:"Open Sans",sans-serif;font-weight:600;font-size:15px;color:var(--red);letter-spacing:.5px;margin-top:-6px}
.main-nav{position:absolute;left:657px;top:103px;display:flex;gap:0;font-family:"Roboto",sans-serif;font-size:10.5px}
.main-nav a{color:var(--white);text-decoration:none;padding:2px 9px;position:relative}
.main-nav a.active::before,.main-nav a.active::after{content:"";position:absolute;top:0;width:3px;height:15px;border:1px solid var(--red)}
.main-nav a.active::before{left:2px;border-right:none}
.main-nav a.active::after{right:2px;border-left:none}

.hero{position:absolute;left:6px;top:139px;width:1188px;height:490px;
  background:linear-gradient(90deg,var(--wood) 0%,#7a5236 14%,#4a3325 22%,var(--sweater) 26%,#a09c98 45%,#8a7f76 60%,#4d3a2e 72%,var(--wood-dark) 100%)}
.hero-quote{position:absolute;left:27px;top:33px;font-size:11px;text-transform:uppercase;letter-spacing:.1px}
.hero-name{position:absolute;left:196px;top:55px;font-size:10.5px;font-weight:600}
.hero-text{position:absolute;left:865px;top:198px;width:300px;font-size:10.2px;line-height:13.9px}
.slider-dots{position:absolute;left:568px;top:475px;display:flex;gap:4px}
.slider-dots span{display:block;width:25px;height:2px;background:#bbb}
.slider-dots span.on{background:var(--red)}

.site-footer{position:absolute;left:6px;top:636px;width:1188px;height:110px;background:var(--black);font-size:10.2px;text-align:center}
.contact{position:absolute;left:0;right:0;top:20px;display:flex;justify-content:center;align-items:center;gap:3px}
.contact svg{width:8px;height:9px;fill:var(--white)}
.rule{position:absolute;left:194px;width:801px;top:48px;height:1px;background:var(--white)}
.legal{position:absolute;left:0;right:0;top:69px;display:flex;justify-content:center;align-items:center;gap:4px}
.legal a{color:var(--white)}
.legal .dot{width:6px;height:6px;border-radius:50%;background:var(--white);margin-left:5px}
</style>
</head>
<body>
<span class="corner tl"></span><span class="corner tr"></span><span class="corner bl"></span><span class="corner br"></span>

<header class="site-header" role="img" aria-label="Kopfbild: Kamera vor unscharfem Waldhintergrund">
  <div class="brand"><span class="brand-name">Velvet Lumen</span></div>
  <nav class="main-nav">
    <a href="#">Willkommen</a>
    <a href="#" class="active">Hinter der Linse</a>
    <a href="#">Portfolio</a>
    <a href="#">Angebote</a>
    <a href="#">Kontakt</a>
  </nav>
</header>

<section class="hero">
  <div class="hero-photo" role="img" aria-label="Fotografin mit Kamera vor einer Holzwand" style="position:absolute;inset:0"></div>
  <p class="hero-quote">„Kreativ, aufgestellt und immer mit dem Herzen dabei“</p>
  <p class="hero-name">Lena Brunner, Fotografin, 35 Jahre alt</p>
  <div class="hero-text">
    <p>Die Welt der Bilder hat mich bereits als Jugendliche in ihren Bann gezogen und daher war die Wahl der Ausbildung für mich schnell klar. Auch nach der Ausbildung zur Fotografin hat mich die Faszination der Fotografie und des Lichtspiels nie losgelassen.</p>
    <p>Fotografie bedeutet für mich: ein festgehaltener Moment, der dokumentiert und die Erinnerung daran somit nie ganz verblassen lässt. Mit der bildgebenden Kunst lassen sich Ihre individuellen Vorstellungen umsetzten und sie bietet unbegrenzte kreative Möglichkeiten.</p>
    <p>In der von Fotografie überladenen digitalen Welt von heute, ist es eine Kunst, Menschen immer noch mit Bildern zu fesseln. Ein gutes Foto ist eine Aufnahme, auf die Sie gerne etwas länger schauen.</p>
    <p>Ich hoffe es gelingt mir, Sie mit dem einen oder anderen Foto, zu fesseln und Ihr Auge zum verweilen einzuladen.</p>
    <p>Wenn Sie Interesse an meinen Dienstleistungen haben, vereinbaren Sie ein unverbindliches Gespräch mit mir. Ich freue mich Sie persönlich kennenzulernen.</p>
  </div>
  <div class="slider-dots"><span></span><span class="on"></span></div>
</section>

<footer class="site-footer">
  <div class="contact">
    <svg viewBox="0 0 8 10"><path d="M4 0a3.5 3.5 0 0 0-3.5 3.5C.5 6 4 10 4 10s3.5-4 3.5-6.5A3.5 3.5 0 0 0 4 0zm0 5a1.4 1.4 0 1 1 0-2.8A1.4 1.4 0 0 1 4 5z"/></svg>
    <span>Talackerstrasse 8 - 6340 Baar</span>
    <svg viewBox="0 0 10 8" style="width:10px"><path d="M0 0h10v8H0zM1 1.2v.4L5 4.6l4-3v-.4zM1 2.8V7h8V2.8L5 5.8z"/></svg>
    <span>hallo@velvet-lumen.ch</span>
    <svg viewBox="0 0 6 10" style="width:6px"><path d="M0 0h6v10H0zM1 1v7h4V1z"/></svg>
    <span>079 555 01 23</span>
  </div>
  <div class="rule"></div>
  <div class="legal">
    <span>© www.velvet-lumen.ch. Alle Rechte vorbehalten.</span>
    <a href="#">AGB</a><span>I</span><a href="#">Links</a><span>I Netzwerk:</span><span class="dot"></span>
  </div>
</footer>
</body>
</html>
```